Professional/Sleek card design for athletic apparel brand

Athletic apparel brand. Mainly focused on lifting weights/gym workouts. Logo and brand are already created. Must use brand logo and name. Creativity is welcome. Looking for a clean, modern, and sexy design.

```html
<!DOCTYPE html>
<html lang="en">
<head>
<meta charset="utf-8">
<title>Grit and Forge – Business Card</title>
<link href="https://fonts.googleapis.com/css2?family=Montserrat:wght@400;500;700&display=swap" rel="stylesheet">
<style>
  :root {
    --backdrop: #3a3a3a;
    --card-dark: #232323;
    --card-light: #ffffff;
    --ink: #1f1f1f;
    --silver: #bdbdbd;
    --pattern-light: #3c3c3c;
    --pattern-mid: #2c2c2c;
  }
  * { margin: 0; padding: 0; box-sizing: border-box; }
  html, body {
    width: 1200px; height: 1200px; overflow: hidden;
    background: var(--backdrop);
    font-family: "Montserrat", sans-serif;
  }
  .stage {
    position: relative; width: 1200px; height: 1200px;
    display: flex; justify-content: center; align-items: center; gap: 60px;
  }
  .card {
    width: 400px; height: 700px; border-radius: 28px;
    position: relative; overflow: hidden;
    box-shadow: 0 18px 40px rgba(0,0,0,0.35);
  }

  /* Back side */
  .card--back { background: var(--card-dark); }
  .card-back__pattern {
    position: absolute; inset: 0;
    background:
      radial-gradient(ellipse 90% 70% at 15% 10%, var(--pattern-light) 0%, rgba(60,60,60,0) 70%),
      radial-gradient(ellipse 70% 50% at 80% 45%, var(--pattern-mid) 0%, rgba(44,44,44,0) 75%),
      linear-gradient(160deg, #303030 0%, var(--card-dark) 65%, #1e1e1e 100%);
  }
  .card-back__brand {
    position: absolute; left: 0; right: 0; top: 540px;
    display: flex; align-items: center; justify-content: center; gap: 10px;
    color: var(--silver); font-weight: 700; font-size: 22px;
    letter-spacing: 2px; text-transform: uppercase; white-space: nowrap;
  }
  .brand-mark { width: 14px; height: 14px; background: currentColor; flex: none; }

  /* Front side */
  .card--front {
    background: var(--card-light); color: var(--ink);
    padding: 0 56px;
  }
  .card-front__brand {
    margin-top: 210px;
    display: flex; align-items: center; justify-content: center; gap: 12px;
    font-weight: 700; font-size: 28px; letter-spacing: 2px;
    text-transform: uppercase; white-space: nowrap;
  }
  .card-front__brand .brand-mark { width: 18px; height: 18px; }
  .person { margin-top: 185px; }
  .person__name { font-weight: 500; font-size: 34px; letter-spacing: 1px; line-height: 1; }
  .person__role { font-size: 18px; letter-spacing: 1px; margin-top: 4px; }
  .contact { list-style: none; margin-top: 24px; font-size: 17px; line-height: 1.25; }
  .contact li { display: flex; align-items: flex-start; gap: 10px; margin-bottom: 4px; }
  .contact svg { width: 16px; height: 16px; flex: none; margin-top: 2px; fill: var(--ink); }
</style>
</head>
<body>
<main class="stage">
  <section class="card card--back">
    <div class="card-back__pattern" role="img" aria-label="Repeating tone-on-tone brand symbol pattern"></div>
    <div class="card-back__brand"><span class="brand-mark"></span>Grit and Forge</div>
  </section>

  <section class="card card--front">
    <div class="card-front__brand"><span class="brand-mark"></span>Grit and Forge</div>
    <div class="person">
      <h1 class="person__name">FULL NAME</h1>
      <p class="person__role">POSITION</p>
    </div>
    <ul class="contact">
      <li><svg viewBox="0 0 16 16"><path d="M3 1l3 3-2 2c1 2 3 4 5 5l2-2 3 3-2 3C6 15 1 10 1 3z"/></svg>(000) 000 0000</li>
      <li><svg viewBox="0 0 16 16"><path d="M1 3h14v10H1z M2 4l6 5 6-5" fill="none" stroke="#1f1f1f" stroke-width="1.5"/></svg>email@company.com</li>
      <li><svg viewBox="0 0 16 16"><g fill="none" stroke="#1f1f1f" stroke-width="1.3"><circle cx="8" cy="8" r="6.5"/><ellipse cx="8" cy="8" rx="3" ry="6.5"/><path d="M1.5 8h13M3 4.5h10M3 11.5h10"/></g></svg>www.company.com</li>
      <li><svg viewBox="0 0 16 16"><path d="M8 1a5 5 0 0 1 5 5c0 4-5 9-5 9S3 10 3 6a5 5 0 0 1 5-5zm0 3a2 2 0 1 0 0 4 2 2 0 0 0 0-4z"/></svg><span>123 Name Street, 000<br>Your City, 00000-000</span></li>
    </ul>
  </section>
</main>
</body>
</html>
```